Pastured Free Range Egg farm needs carton label

We have recently updated our logo, and are looking to incorporate the new logo into a new design for our dozen size egg cartons. (New logo has been included in the uploads - there are several file formats available, so let me know if you need a different file format for the logo.)
We are a company that is focused on ethical farming, and the welfare of our hens. We are a small, niche farm, run by a husband and wife and 3 children.
I have included a photo of our farm and the trailers we use for our hens so that you can see the type of farming methods we use.
We would like to keep the label relaxed, to reflect the small family business.
We would like the use of green colours to represent the "pastured" aspect of our egg farming. We want the label to represent our better farming practices.
We have included a graphic of our current label which we like the feel and style of.
We have also included a graphic of the dieline that must be used so we can submit the design to the printing company. (we do not need a space for a barcode on our label)
______________
Things that must be included legally on the label:
* The words "12 Pastured Free Range Eggs",
*Nutrition label panel as pictured in the current label graphic
* Weight options as pictured in the current label the words "Min Total Mass" must be used and have a selection for weights of 600gm, 700gm and 800gm
* Chicken stocking density must be prominent to show our care for the hens the words "150 chickens per hectare" must be used
* A best before section where we can stamp a date
* A product of Australia logo
* The words "Commercial reuse of this carton prohibited" on the back of the carton
* A "please recycle" logo on the back of the carton
* Farm details on the back of the carton:
Marlow Farm
T & K Marlow
18 Pemberly Rd
Ashvale VIC 3762
Ph: 0491 578 306
I would like some information on our farming practices like what is pictured on the original label:
" Our hens are housed in mobile trailers that are moved to fresh pasture regularly on our farm in Ashvale, Victoria.
The hens have access to the outdoors 24 hours a day. They have plenty of room to flap their wings, and to scratch and forage for bugs.
Our hens are happy and healthy, help to sustain our land, and lay us these delicious eggs!"
Target Market(s)
People wanting ethical sustainable produce
Look and feel

```html
<!DOCTYPE html>
<html lang="en">
<head>
<meta charset="utf-8">
<title>Marlow Farm – Dozen Egg Carton Label</title>
<link rel="stylesheet" href="https://fonts.googleapis.com/css2?family=Open+Sans:wght@400;600;700&family=Caveat:wght@700&display=swap">
<style>
  :root{
    --pasture:#4a675c;
    --olive:#858200;
    --ink:#1f1f1f;
    --dieline:#e0338f;
    --paper:#ffffff;
    --window:#c8e8f8;
    --table-green:#a8d98c;
    --table-light:#e6f4dc;
  }
  *{box-sizing:border-box;margin:0;padding:0}
  html,body{width:1200px;height:1199px;overflow:hidden;background:var(--paper)}
  body{position:relative;font-family:"Open Sans",sans-serif;color:var(--pasture)}

  /* ---------- shared front label ---------- */
  .label{position:absolute;width:1049px;height:302px;overflow:hidden;background:var(--paper)}
  .label--sample{left:74px;top:135px;border:1.5px solid var(--ink);border-radius:40px}
  .label--lid{left:61px;top:660px;border:1px solid var(--dieline);border-radius:40px 0 40px 40px;border-bottom-style:dashed}
  .farm-sketch{position:absolute;left:27px;top:4px;width:305px;height:294px;
    background:radial-gradient(ellipse at 45% 45%,#c9d6cf 0%,#e4ebe7 55%,rgba(255,255,255,0) 78%)}
  .band{position:absolute;left:0;top:0;width:1049px;height:302px}
  .best-before{position:absolute;right:553px;top:11px;font-size:11px;font-weight:600;letter-spacing:.06em}
  .happy-hens{position:absolute;right:553px;top:30px;font-family:"Caveat",cursive;font-size:25px;color:var(--olive);line-height:1}
  .practice{position:absolute;right:553px;top:69px;text-align:right;font-size:8.8px;line-height:11.8px;color:var(--ink);white-space:nowrap}
  .divider{position:absolute;left:506px;top:71px;width:1px;height:137px;background:var(--pasture)}
  .density{position:absolute;left:518px;top:56px}
  .density__num{font-family:"Caveat",cursive;font-size:86px;line-height:.9;color:var(--olive);letter-spacing:-2px}
  .density__unit{font-size:9px;font-weight:600;letter-spacing:.04em;margin-top:2px}
  .brand-mark{position:absolute;left:771px;top:53px;width:110px;height:110px;border-radius:50%;background:var(--pasture)}
  .brand-name{position:absolute;left:694px;top:180px;font-size:40px;font-weight:700;color:var(--ink);white-space:nowrap}
  .count{position:absolute;left:466px;top:229px;width:80px;height:56px;border-radius:50%;background:var(--paper);border:1.5px solid var(--olive);
    font-size:42px;font-weight:400;color:var(--pasture);text-align:center;line-height:52px;letter-spacing:-3px}
  .product{position:absolute;left:559px;top:238px;font-size:34px;font-weight:700;color:var(--paper);white-space:nowrap}

  /* ---------- back panel (printed upside down) ---------- */
  .back{position:absolute;left:106px;top:525px;width:958px;height:135px;border:1px solid var(--dieline);border-bottom:none;border-radius:26px 26px 0 0}
  .flip{position:absolute;transform:rotate(180deg)}
  .nutrition{left:60px;top:8px;width:206px;height:88px;border:1px solid var(--table-green);font-size:5px;color:var(--ink);border-collapse:collapse}
  .nutrition caption{caption-side:top;font-weight:700;text-align:left;padding:1px 2px;font-size:6px}
  .nutrition td,.nutrition th{border:1px solid #fff;padding:0 2px;text-align:left;font-weight:400}
  .nutrition tr:nth-child(odd) td{background:var(--table-light)}
  .nutrition th{background:var(--table-green);font-weight:700}
  .pack-sizes{left:280px;top:45px;width:78px;height:53px;border:1px solid var(--table-green);background:var(--table-light);font-size:5.5px;color:var(--ink);padding:3px;line-height:8px}
  .vline{position:absolute;width:1px;background:var(--pasture)}
  .recycle{left:400px;top:10px;width:138px;height:27px;display:flex;align-items:center;gap:8px;font-size:10px;letter-spacing:.18em;color:var(--ink);white-space:nowrap}
  .recycle__dot{width:26px;height:26px;border-radius:50%;background:var(--pasture);flex:none}
  .reuse{left:406px;top:64px;width:112px;font-size:10.5px;line-height:17px;color:var(--ink);font-weight:400;white-space:nowrap;text-align:left}
  .farm-details{left:548px;top:12px;width:96px;font-size:10.5px;line-height:17px;color:var(--ink);white-space:nowrap;font-style:normal}
  .origin-badge{position:absolute;left:684px;top:12px;width:56px;height:86px;border:1.5px solid #1b8a66;border-radius:5px}
  .back-brand{left:784px;top:10px;width:118px;height:91px;display:flex;flex-direction:column;align-items:center;gap:6px}
  .back-brand__dot{width:52px;height:52px;border-radius:50%;background:var(--pasture)}
  .back-brand__name{font-size:17px;font-weight:700;color:var(--ink);white-space:nowrap}

  /* ---------- base panel ---------- */
  .base{position:absolute;left:106px;top:960px;width:958px;height:137px;border:1px solid var(--dieline);border-top:none;border-radius:0 0 14px 14px}
  .window{position:absolute;top:10px;width:85px;height:80px;background:var(--window);border:1px solid var(--dieline);border-radius:6px}
  .base-brand{position:absolute;left:141px;top:32px;width:112px;display:flex;flex-direction:column;align-items:center;gap:5px}
  .base-brand__dot{width:46px;height:46px;border-radius:50%;background:var(--pasture)}
  .base-brand__name{font-size:17px;font-weight:700;color:var(--ink);white-space:nowrap}
  .weights{position:absolute;left:293px;top:36px;list-style:none}
  .weights li{display:flex;align-items:center;gap:9px;height:23.5px;font-size:15px}
  .weights li::before{content:"";width:24px;height:16px;border:1.5px solid var(--olive);border-radius:50%}
  .min-mass{position:absolute;left:288px;top:111px;width:95px;text-align:center;font-size:11px;font-weight:700}
  .base-band{position:absolute;left:0;top:0;width:958px;height:152px;overflow:visible}
  .base .count{left:421px;top:52px;width:76px;height:54px;line-height:50px;font-size:40px}
  .base .product{left:506px;top:79px;font-size:31px}
</style>
</head>
<body>

<!-- sample label -->
<section class="label label--sample">
  <div class="farm-sketch" role="img" aria-label="Pencil sketch of a hen foraging under trees beside a mobile hen trailer"></div>
  <svg class="band" viewBox="0 0 1049 302" aria-hidden="true"><path d="M196,302 C400,250 600,228 800,225 C900,224 1000,240 1049,262 L1049,302 Z" fill="var(--pasture)"/></svg>
  <p class="best-before">BEST BEFORE</p>
  <h2 class="happy-hens">Happy Hens</h2>
  <p class="practice">"Our hens are housed in mobile<br>trailers that are moved to fresh<br>pasture regularly on our farm in<br>Ashvale, Victoria.<br>The hens have access to the<br>outdoors 24 hours a day.<br>They have plenty of room to<br>flap their wings, and to<br>scratch and forage for bugs.<br>Our hens are happy and healthy,<br>help to sustain our land,<br>and lay us these delicious eggs!"</p>
  <span class="divider"></span>
  <div class="density"><div class="density__num">150</div><div class="density__unit">chickens per hectare</div></div>
  <span class="brand-mark"></span>
  <p class="brand-name">Marlow Farm</p>
  <div class="count">12</div>
  <p class="product">Pastured Free Range Eggs</p>
</section>

<!-- carton dieline: back panel -->
<section class="back">
  <table class="flip nutrition">
    <caption>Nutrition Information – Servings per pack: 12</caption>
    <tr><th>Avg qty</th><th>600g</th><th>700g</th><th>800g</th><th>100g</th></tr>
    <tr><td>Energy</td><td>260kJ</td><td>300kJ</td><td>345kJ</td><td>520kJ</td></tr>
    <tr><td>Protein</td><td>6.3g</td><td>7.3g</td><td>8.4g</td><td>12.6g</td></tr>
    <tr><td>Fat, total</td><td>4.8g</td><td>5.6g</td><td>6.4g</td><td>9.6g</td></tr>
    <tr><td>Saturated</td><td>1.4g</td><td>1.6g</td><td>1.9g</td><td>2.8g</td></tr>
    <tr><td>Carbohydrate</td><td>0.2g</td><td>0.2g</td><td>0.3g</td><td>0.4g</td></tr>
    <tr><td>Sugars</td><td>0.2g</td><td>0.2g</td><td>0.3g</td><td>0.4g</td></tr>
    <tr><td>Sodium</td><td>66mg</td><td>77mg</td><td>88mg</td><td>132mg</td></tr>
  </table>
  <div class="flip pack-sizes"><strong>Pack serving sizes:</strong><br>600g: 50g eggs<br>700g: 58g eggs<br>800g: 67g eggs</div>
  <span class="vline" style="left:381px;top:12px;height:88px"></span>
  <div class="flip recycle"><span class="recycle__dot"></span><span>PLEASE RECYCLE</span></div>
  <p class="flip reuse">Commercial reuse of<br>this carton prohibited</p>
  <span class="vline" style="left:532px;top:38px;height:62px"></span>
  <address class="flip farm-details">Marlow Farm<br>T &amp; K Marlow<br>18 Pemberly Rd<br>Ashvale VIC 3762<br>Ph: 0491 578 306</address>
  <span class="vline" style="left:661px;top:12px;height:88px"></span>
  <span class="origin-badge"></span>
  <span class="vline" style="left:764px;top:12px;height:88px"></span>
  <div class="flip back-brand"><span class="back-brand__dot"></span><span class="back-brand__name">Marlow Farm</span></div>
</section>

<!-- carton dieline: lid front -->
<section class="label label--lid">
  <div class="farm-sketch" role="img" aria-label="Pencil sketch of a hen foraging under trees beside a mobile hen trailer"></div>
  <svg class="band" viewBox="0 0 1049 302" aria-hidden="true"><path d="M196,302 C400,250 600,228 800,225 C900,224 1000,240 1049,262 L1049,302 Z" fill="var(--pasture)"/></svg>
  <p class="best-before">BEST BEFORE</p>
  <h2 class="happy-hens">Happy Hens</h2>
  <p class="practice">"Our hens are housed in mobile<br>trailers that are moved to fresh<br>pasture regularly on our farm in<br>Ashvale, Victoria.<br>The hens have access to the<br>outdoors 24 hours a day.<br>They have plenty of room to<br>flap their wings, and to<br>scratch and forage for bugs.<br>Our hens are happy and healthy,<br>help to sustain our land,<br>and lay us these delicious eggs!"</p>
  <span class="divider"></span>
  <div class="density"><div class="density__num">150</div><div class="density__unit">chickens per hectare</div></div>
  <span class="brand-mark"></span>
  <p class="brand-name">Marlow Farm</p>
  <div class="count">12</div>
  <p class="product">Pastured Free Range Eggs</p>
</section>

<!-- carton dieline: base panel -->
<section class="base">
  <svg class="base-band" viewBox="0 0 958 152" aria-hidden="true"><path d="M459,152 L459,72 C600,62 800,66 958,95 L958,132 Q958,152 936,152 Z" fill="var(--pasture)"/></svg>
  <span class="window" style="left:46px"></span>
  <span class="window" style="left:826px"></span>
  <div class="base-brand"><span class="base-brand__dot"></span><span class="base-brand__name">Marlow Farm</span></div>
  <span class="vline" style="left:271px;top:35px;height:88px"></span>
  <ul class="weights"><li>600gm</li><li>700gm</li><li>800gm</li></ul>
  <p class="min-mass">Min Total Mass</p>
  <span class="vline" style="left:395px;top:35px;height:88px"></span>
  <div class="count">12</div>
  <p class="product">Pastured Free Range Eggs</p>
</section>

</body>
</html>
```